Real Estate investment company needs billboard designs

This is our website: https://velmarkpropertygroup.com/
We are looking for some billboard concepts that uses our CEO in the design. I have attached some images and 1 billboard design that someone in our industry uses, but we don't want it exactly like his.

Industry/Entity Type

real estate

Colors

Designer to choose colors to be used in the design.

Requirements
Must have
• Company colors from websiute

```html
<!DOCTYPE html>
<html lang="en">
<head>
<meta charset="utf-8">
<title>Velmark Property Group – Billboard</title>
<link href="https://fonts.googleapis.com/css2?family=DM+Serif+Display&family=Oswald:wght@500;600&family=Roboto+Condensed:wght@700;800&display=swap" rel="stylesheet">
<style>
  :root {
    --page: #eef1f4;
    --sky-top: #8ec5ec;
    --sky-bottom: #e3f1fb;
    --navy: #141a48;
    --navy-soft: #232b66;
    --red: #e0242a;
    --white: #ffffff;
  }
  * { margin: 0; padding: 0; box-sizing: border-box; }
  html, body { width: 1200px; height: 962px; overflow: hidden; background: var(--page); }

  .billboard {
    position: absolute; left: 40px; top: 161px;
    width: 1120px; height: 640px; overflow: hidden;
    background: linear-gradient(180deg, var(--sky-top), var(--sky-bottom));
    box-shadow: 0 10px 30px rgba(20, 26, 72, 0.2);
  }
  .billboard__art { position: absolute; inset: 0; }

  .brand {
    position: absolute; left: 540px; top: 44px;
    display: flex; align-items: center; gap: 12px;
    font-family: "Oswald", sans-serif; font-weight: 600;
    font-size: 28px; line-height: 1; color: var(--navy);
    text-transform: uppercase; letter-spacing: 1px;
    white-space: nowrap;
  }
  .brand__mark { width: 18px; height: 18px; background: var(--red); }

  .pitch { position: absolute; left: 540px; top: 118px; width: 540px; color: var(--navy); }
  .pitch__headline {
    font-family: "DM Serif Display", serif; font-size: 88px;
    line-height: 0.98; letter-spacing: -1px;
  }
  .pitch__headline .accent { color: var(--red); }
  .pitch__offer {
    margin-top: 22px;
    font-family: "Roboto Condensed", sans-serif; font-weight: 700;
    font-size: 28px; line-height: 1.25; color: var(--navy-soft);
  }
  .pitch__call {
    margin-top: 18px;
    font-family: "Roboto Condensed", sans-serif; font-weight: 800;
    font-size: 50px; line-height: 1; white-space: nowrap;
  }

  .web {
    position: absolute; left: 540px; top: 564px;
    font-family: "Roboto Condensed", sans-serif; font-weight: 800;
    font-size: 40px; line-height: 52px; color: var(--white);
    white-space: nowrap;
  }
</style>
</head>
<body>
  <section class="billboard" aria-label="Velmark Property Group billboard">
    <svg class="billboard__art" width="1120" height="640" viewBox="0 0 1120 640">
      <defs>
        <linearGradient id="ceo" x1="0" y1="0" x2="0" y2="1">
          <stop offset="0" stop-color="#c99a80"/>
          <stop offset="0.34" stop-color="#bb8d74"/>
          <stop offset="0.4" stop-color="#3a3b40"/>
          <stop offset="1" stop-color="#2b2c31"/>
        </linearGradient>
      </defs>
      <polygon class="navy-field" points="0,0 470,0 400,640 0,640" fill="var(--navy)"/>
      <rect class="ceo-photo" x="60" y="70" width="330" height="570" rx="4" fill="url(#ceo)" role="img" aria-label="Portrait of the company CEO in a dark polo shirt, arms crossed"/>
      <polygon class="web-band" points="420,540 1120,540 1120,640 408,640" fill="var(--red)"/>
    </svg>

    <div class="brand"><span class="brand__mark"></span><span>Velmark Property Group</span></div>

    <div class="pitch">
      <div class="pitch__headline">Need to Sell<br><span class="accent">Fast?</span></div>
      <div class="pitch__offer">We buy houses as-is.<br>Fair cash offer within 24 hours.</div>
      <div class="pitch__call">Call 865-555-0193</div>
    </div>

    <div class="web">velmarkpropertygroup.com</div>
  </section>
</body>
</html>
```